Unique E-commerce website needs a FLAT UI design

Looking for creative website designer / company to design a flat ui interface for the main 4 pages.

I SEEK FLAT UI DESIGN ONLY - this means nice, clean and modern design,

As we're dealing with the design of the main pages this will define the overall site design so take a moment or two to think on the audience and create an appealing branding.

Website design must be mobile/ipad friendly.

I've written a detailed design requirements document for those 4 pages.
Please read it carefully and make sure you understand every aspect of it before starting the design process.
You can find a brief intro text and some reference designs that I like to get you started.

This is not a closed concept, I'm open to hear new ideas and ways to improve the UI/UX.

Feel free to ask anything, I'm available most of the day.

I'm looking to build a long term relationship as this is the first phase of the design, I have 1-2 phases to come.

Target Market(s)

Online shoppers age between 18-60 that buy frequently at US merchants

Industry/Entity Type

It Company

Number of Pages Required

4 page

Requirements
Must have
• Flat UI design
• Flat colors
• Modern, clean and easy to follow design
Nice to have
• Original icons for the features page

```html
<!DOCTYPE html>
<html lang="en">
<head>
<meta charset="utf-8">
<title>Parcelo Home</title>
<link rel="stylesheet" href="https://fonts.googleapis.com/css2?family=Roboto:wght@400;500;700&family=Lato:wght@400;700&display=swap">
<style>
:root{
  --blue:#2f85c9;
  --blue-dark:#2574b3;
  --black:#060606;
  --ink:#222;
  --muted:#555;
  --light:#efefef;
  --card:#eaeaea;
  --white:#fff;
  --footer-bar:#2b2b2b;
}
*{box-sizing:border-box;margin:0;padding:0}
html,body{width:1200px;height:2994px;overflow:hidden}
body{font-family:"Lato",sans-serif;color:var(--ink);background:var(--white);position:relative}
.wrap{position:relative;width:956px;margin:0 auto}
h2.section-title{font-family:"Roboto",sans-serif;font-weight:500;font-size:30px;text-align:center;color:var(--ink)}
.section-sub{font-size:14px;color:var(--blue);text-align:center;margin-top:10px}
.divider{position:relative;width:420px;height:18px;margin:10px auto 0}
.divider::before{content:"";position:absolute;left:0;right:0;top:9px;height:1px;background:#cfcfcf}
.divider span{position:absolute;left:50%;top:2px;width:14px;height:14px;margin-left:-7px;transform:rotate(45deg);border:1px solid #cfcfcf;background:inherit}

/* top bar */
.topbar{height:35px;background:var(--blue);display:flex;justify-content:flex-end;align-items:center;padding-right:180px;gap:26px;color:#fff;font-size:13px}
.topbar .item{display:flex;align-items:center;gap:7px}
.lang{background:#fff;color:var(--ink);padding:4px 12px;display:flex;gap:8px;align-items:center;font-size:12px}
.lang i{width:16px;height:10px;background:var(--blue);display:block}

/* header */
.header{height:90px;background:var(--black);position:relative}
.brand{position:absolute;left:120px;top:20px;display:flex;flex-direction:column;align-items:flex-start;gap:6px}
.brand .mark{width:22px;height:22px;background:var(--blue);margin-left:40px}
.brand .name{font-family:"Roboto",sans-serif;font-weight:700;font-size:22px;color:#fff;letter-spacing:.5px}
.nav{position:absolute;right:120px;top:47px;display:flex;gap:6px;font-size:13px;font-family:"Roboto",sans-serif}
.nav a{color:#fff;text-decoration:none;padding:9px 12px}
.nav a.active{background:var(--blue)}

/* hero */
.hero{height:520px;position:relative;background:linear-gradient(100deg,#cbbfa8 0%,#d9d2c6 35%,#e6e9ec 60%,#cfd6de 100%)}
.hero-text{position:absolute;top:210px;width:100%;text-align:center;font-family:"Roboto",sans-serif;font-weight:500;color:#111}
.hero-text .l1{font-size:38px}
.hero-text .l2{font-size:38px;margin-top:18px}
.hero-form{position:absolute;top:355px;left:137px;display:flex;gap:12px}
.hero-form .field{width:305px;height:52px;background:#fff;border:1px solid #ddd;font-size:13px;color:#999;padding:18px 12px}
.hero-form .btn{width:275px;height:52px;margin-left:8px;background:var(--blue);color:#fff;font-family:"Roboto",sans-serif;font-weight:700;font-size:16px;display:flex;align-items:center;justify-content:center}

/* what we do */
.what{height:590px;padding-top:52px;background:var(--white)}
.services{display:flex;justify-content:space-between;margin-top:30px}
.service{width:267px;position:relative;padding-top:65px}
.service .box{height:180px;background:var(--card);text-align:center;padding:80px 20px 0}
.service.active .box{background:var(--blue);color:#fff}
.service h3{font-family:"Roboto",sans-serif;font-weight:500;font-size:18px}
.service p{font-size:12px;font-weight:700;margin-top:20px;line-height:18px}
.service .diamond{position:absolute;left:50%;top:10px;width:88px;height:88px;margin-left:-44px;transform:rotate(45deg);background:var(--blue);border:4px solid #fff;box-shadow:0 0 0 1px #d0d0d0}
.service .icon{position:absolute;left:50%;top:34px;margin-left:-20px;width:40px;height:40px}
.what .lead{font-size:12px;line-height:18px;color:var(--muted);margin-top:46px}

/* pricing */
.pricing{height:641px;background:var(--light);padding-top:55px}
.plans{display:flex;justify-content:space-between;margin-top:38px}
.plan{width:305px;height:424px;background:#fff;box-shadow:0 0 4px rgba(0,0,0,.2);position:relative}
.plan h3{height:50px;background:var(--blue);color:#fff;font-family:"Roboto",sans-serif;font-weight:500;font-size:20px;display:flex;align-items:center;justify-content:center}
.plan.featured h3{background:var(--blue-dark)}
.plan ul{list-style:none;margin-top:8px}
.plan li{height:52px;display:flex;align-items:center;padding-left:16px;font-size:13px;color:var(--muted);gap:10px}
.plan li:nth-child(odd){background:#f1f1f1}
.plan li.hi{background:var(--blue);color:#fff}
.plan .tick{width:12px;height:12px;flex:none}
.plan .cta{position:absolute;bottom:22px;left:50%;transform:translateX(-50%);width:225px;height:52px;background:var(--black);color:#fff;font-family:"Roboto",sans-serif;font-weight:500;font-size:16px;display:flex;align-items:center;justify-content:center}
.plan .cta.blue{background:var(--blue)}

/* offers */
.offers{height:307px;background:linear-gradient(90deg,#2c2721,#4a3f33 40%,#3a332a 70%,#2a2520);position:relative}
.offers .wrap{display:flex;justify-content:space-between;padding-top:50px}
.offer{width:454px;height:210px;border:2px solid #e6e6e6;text-align:center;color:#fff;font-family:"Roboto",sans-serif;padding-top:38px}
.offer .txt{font-size:20px;line-height:32px}
.offer .num{display:flex;justify-content:center;align-items:flex-end;gap:6px;margin-top:6px}
.offer .num b{font-size:66px;color:var(--blue);font-weight:700;line-height:66px}
.offer .num span{font-size:22px;font-weight:700;text-align:left;line-height:26px;padding-bottom:4px}

/* brands */
.brands{height:280px;padding-top:50px}
.brand-row{display:flex;align-items:center;justify-content:space-between;margin-top:28px;width:1010px;margin-left:-27px}
.arrow{width:24px;height:24px}
.brand-tile{width:150px;height:74px;border:1px solid #ddd;display:flex;align-items:center;justify-content:center;font-family:"Roboto",sans-serif;font-weight:700;font-size:22px;color:var(--ink)}

/* get started */
.start{height:254px;background:var(--blue);padding-top:48px;color:#fff}
.start h2.section-title{color:#fff}
.start .section-sub{color:#fff}
.start .divider::before{background:#9cc6e6}
.start .divider span{border-color:#9cc6e6;background:var(--blue)}
.start .btn{width:226px;height:52px;margin:28px auto 0;background:var(--black);font-family:"Roboto",sans-serif;font-weight:500;font-size:15px;display:flex;align-items:center;justify-content:center}

/* footer */
.footer{height:245px;background:var(--black);color:#fff;padding-top:32px}
.footer .wrap{display:flex}
.fcol{border-right:1px solid #333;padding-right:20px}
.fcol:last-child{border-right:0}
.fcol h4{font-family:"Roboto",sans-serif;font-weight:500;font-size:15px;padding-bottom:8px;border-bottom:1px solid #444;margin-bottom:12px}
.fcol p,.fcol li{font-size:11px;line-height:16px}
.fcol ul{list-style:none}
.links{display:grid;grid-template-columns:140px 80px;row-gap:14px;font-size:11px}
.contact-row{display:flex;gap:10px;margin-bottom:12px;align-items:flex-start}
.contact-row svg{flex:none}
.input{width:190px;height:22px;background:#fff;color:#888;font-size:10px;padding:5px 6px;margin-top:8px}
.sub-btn{display:inline-block;background:var(--blue);font-size:11px;padding:4px 8px;margin-top:8px}
.social li{display:flex;align-items:center;gap:10px;margin-bottom:16px}
.social i{width:18px;height:18px;border-radius:50%;background:#fff;display:block}
.bottombar{height:32px;background:var(--footer-bar);display:flex;justify-content:space-between;align-items:center;padding:0 122px;color:#fff;font-size:12px}
.bottombar .pay{font-family:"Lato",sans-serif;font-weight:700;font-size:15px}
</style>
</head>
<body>

<div class="topbar">
  <div class="item"><svg width="14" height="14" viewBox="0 0 14 14"><circle cx="7" cy="4" r="3" fill="#fff"/><path d="M1 14c0-4 3-6 6-6s6 2 6 6z" fill="#fff"/></svg>Login</div>
  <div class="item"><svg width="14" height="14" viewBox="0 0 14 14"><path d="M2 2h6v10H2z" fill="none" stroke="#fff" stroke-width="1.5"/><path d="M7 7h6M10 4l3 3-3 3" stroke="#fff" stroke-width="1.5" fill="none"/></svg>Sign Up</div>
  <div class="lang"><i></i>English</div>
</div>

<header class="header">
  <div class="brand"><span class="mark"></span><span class="name">PARCELO HOME</span></div>
  <nav class="nav">
    <a class="active">Home</a><a>Features</a><a>Pricing</a><a>Help &amp; Support</a><a>~ Shipping Calculator</a>
  </nav>
</header>

<section class="hero" role="img" aria-label="Photo of a smiling courier handing a parcel to a woman signing for the delivery">
  <div class="hero-text"><div class="l1">WE PROVIDE 100%</div><div class="l2">SAFE &amp; SECURE PRODUCT IN YOUR HOME</div></div>
  <div class="hero-form">
    <div class="field">Email Address</div>
    <div class="field">Password</div>
    <div class="btn">RAPID ACCOUND CREATION</div>
  </div>
</section>

<section class="what">
  <div class="wrap">
    <h2 class="section-title">WHAT WE DO</h2>
    <p class="section-sub">Lorem ipsum dolor sit amet, consectetur Donec a consequat mag&nbsp; Aenean eu velit&nbsp; Aenean sollicitudin</p>
    <div class="divider"><span style="background:#fff"></span></div>
    <div class="services">
      <div class="service active">
        <div class="diamond"></div>
        <svg class="icon" viewBox="0 0 40 40"><rect x="4" y="12" width="20" height="14" fill="#fff"/><path d="M24 16h7l5 6v4H24z" fill="#fff"/><circle cx="11" cy="28" r="3.5" fill="#fff" stroke="#2f85c9" stroke-width="1.5"/><circle cx="30" cy="28" r="3.5" fill="#fff" stroke="#2f85c9" stroke-width="1.5"/></svg>
        <div class="box"><h3>Ship it Over</h3><p>Lorem ipsum dolor sit amet, consectetur Donec a consequat mag.</p></div>
      </div>
      <div class="service">
        <div class="diamond"></div>
        <svg class="icon" viewBox="0 0 40 40"><rect x="10" y="6" width="4" height="28" fill="#fff"/><rect x="10" y="6" width="22" height="3" fill="#fff"/><path d="M28 9v8" stroke="#fff" stroke-width="1.5"/><rect x="24" y="17" width="8" height="7" fill="#fff"/><rect x="6" y="32" width="14" height="3" fill="#fff"/></svg>
        <div class="box"><h3>We do the heavy lifting</h3><p>Lorem ipsum dolor sit amet, consectetur Donec a consequat mag.</p></div>
      </div>
      <div class="service">
        <div class="diamond"></div>
        <svg class="icon" viewBox="0 0 40 40"><rect x="13" y="8" width="14" height="12" fill="#fff"/><path d="M4 26h10l6 3h10l6-4v4l-8 5H4z" fill="#fff"/></svg>
        <div class="box"><h3>Track delivery</h3><p>Lorem ipsum dolor sit amet, consectetur Donec a consequat mag.</p></div>
      </div>
    </div>
    <p class="lead">Lorem ipsum dolor sit amet, consectetuer adipiscing elit, sed diam nonummy nibh euismod tincidunt ut laoreet dolore magna aliquam erat volutpat. Ut wisi enim ad minim veniam, quis nostrud exerci tation ullamcorper suscipit lobortis nisl ut aliquip ex ea commodo consequat. Duis autem vel eum iriure dolor in hendrerit in vulputate velit esse molestie consequat, vel illum dolore eu feugiat nulla facilisis at vero eros et accumsan et iusto odio dignissim qui blandit praesent luptatum zzril delenit augue duis dolore te feugait nulla facilisi.</p>
  </div>
</section>

<section class="pricing">
  <div class="wrap">
    <h2 class="section-title">OUR PRICING</h2>
    <p class="section-sub">Lorem ipsum dolor sit amet, consectetur Donec a consequat mag&nbsp; Aenean eu velit&nbsp; Aenean sollicitudin</p>
    <div class="divider"><span style="background:#efefef"></span></div>
    <div class="plans">
      <div class="plan">
        <h3>PACKAGE RELATED</h3>
        <ul>
          <li><svg class="tick" viewBox="0 0 12 12"><path d="M1 6l3 3 7-7" stroke="currentColor" stroke-width="2" fill="none"/></svg>Package Processing $1</li>
          <li><svg class="tick" viewBox="0 0 12 12"><path d="M1 6l3 3 7-7" stroke="currentColor" stroke-width="2" fill="none"/></svg>Payment Processing 4% of shipping costs</li>
          <li><svg class="tick" viewBox="0 0 12 12"><path d="M1 6l3 3 7-7" stroke="currentColor" stroke-width="2" fill="none"/></svg>Storage $1&nbsp; costs</li>
        </ul>
        <div class="cta">SIGN UP FOR FREE</div>
      </div>
      <div class="plan featured">
        <h3>EXTRA SERVICES</h3>
        <ul>
          <li><svg class="tick" viewBox="0 0 12 12"><path d="M1 6l3 3 7-7" stroke="currentColor" stroke-width="2" fill="none"/></svg>Photos starting from $2&nbsp; Costs</li>
          <li class="hi"><svg class="tick" viewBox="0 0 12 12"><path d="M1 6l3 3 7-7" stroke="currentColor" stroke-width="2" fill="none"/></svg>Repacking $5</li>
          <li><svg class="tick" viewBox="0 0 12 12"><path d="M1 6l3 3 7-7" stroke="currentColor" stroke-width="2" fill="none"/></svg>Filling Out Customs Form $5</li>
          <li><svg class="tick" viewBox="0 0 12 12"><path d="M1 6l3 3 7-7" stroke="currentColor" stroke-width="2" fill="none"/></svg>Express Checkout $5</li>
          <li><svg class="tick" viewBox="0 0 12 12"><path d="M1 6l3 3 7-7" stroke="currentColor" stroke-width="2" fill="none"/></svg>Custom Requests $5</li>
        </ul>
        <div class="cta blue">LEARN MORE</div>
      </div>
      <div class="plan">
        <h3>EXTRA SERVICES</h3>
        <ul>
          <li><svg class="tick" viewBox="0 0 12 12"><path d="M1 6l3 3 7-7" stroke="currentColor" stroke-width="2" fill="none"/></svg>Missing Mailbox Number $2</li>
          <li><svg class="tick" viewBox="0 0 12 12"><path d="M1 6l3 3 7-7" stroke="currentColor" stroke-width="2" fill="none"/></svg>Heavy Package $10 more then 50 lbs</li>
          <li><svg class="tick" viewBox="0 0 12 12"><path d="M1 6l3 3 7-7" stroke="currentColor" stroke-width="2" fill="none"/></svg>Return Label Processing $5</li>
        </ul>
        <div class="cta">LEARN MORE</div>
      </div>
    </div>
  </div>
</section>

<section class="offers" role="img" aria-label="Dark warehouse photo of stacked cardboard boxes">
  <div class="wrap">
    <div class="offer"><div class="txt">You have a ordering more<br>than 1 service get a</div><div class="num"><b>10</b><span>%<br>OFF</span></div></div>
    <div class="offer"><div class="txt">You ordering extra service for<br>every incoming package Get a</div><div class="num"><b>15</b><span>%<br>OFF</span></div></div>
  </div>
</section>

<section class="brands">
  <div class="wrap">
    <h2 class="section-title">FEATURED US BRANDS</h2>
    <p class="section-sub">Lorem ipsum dolor sit amet, consectetur Donec a consequat mag&nbsp; Aenean eu velit&nbsp; Aenean sollicitudin</p>
    <div class="divider"><span style="background:#fff"></span></div>
    <div class="brand-row">
      <svg class="arrow" viewBox="0 0 24 24"><circle cx="12" cy="12" r="10" fill="none" stroke="#555" stroke-width="1.5"/><path d="M14 7l-5 5 5 5" fill="none" stroke="#555" stroke-width="2"/></svg>
      <div class="brand-tile">Shopwell</div>
      <div class="brand-tile">Marketa</div>
      <div class="brand-tile">Craftly</div>
      <div class="brand-tile">Tinywear</div>
      <div class="brand-tile">Loomry</div>
      <svg class="arrow" viewBox="0 0 24 24"><circle cx="12" cy="12" r="10" fill="none" stroke="#555" stroke-width="1.5"/><path d="M10 7l5 5-5 5" fill="none" stroke="#555" stroke-width="2"/></svg>
    </div>
  </div>
</section>

<section class="start">
  <div class="wrap">
    <h2 class="section-title">GET STARTED</h2>
    <p class="section-sub">Lorem ipsum dolor sit amet, consectetur Donec a consequat mag&nbsp; Aenean eu velit&nbsp; Aenean sollicitudin</p>
    <div class="divider"><span></span></div>
    <div class="btn">GET STARTED NOW</div>
  </div>
</section>

<footer class="footer">
  <div class="wrap">
    <div class="fcol" style="width:255px">
      <h4>Overview</h4>
      <div class="links"><span>Feature</span><span>About Us</span><span>Pricing</span><span>Contact Us</span><span>Package Calculator</span><span></span><span>Marketa Calculator</span></div>
    </div>
    <div class="fcol" style="width:270px;padding-left:20px">
      <h4>Contact Address</h4>
      <div class="contact-row"><svg width="12" height="14" viewBox="0 0 12 14"><path d="M6 0a5 5 0 0 1 5 5c0 4-5 9-5 9S1 9 1 5a5 5 0 0 1 5-5z" fill="#fff"/><circle cx="6" cy="5" r="2" fill="#060606"/></svg><p><b>Lorem ipsum dolor sit amet,</b><br>consectetuer adipiscing elit,<br>sed diam nonummy nibh</p></div>
      <div class="contact-row"><svg width="14" height="12" viewBox="0 0 14 12"><path d="M1 3h12v8H1z" fill="#fff"/><path d="M3 3V1h8v2" stroke="#fff" fill="none"/></svg><p>0123-555-014</p></div>
      <div class="contact-row"><svg width="14" height="10" viewBox="0 0 14 10"><rect width="14" height="10" fill="#fff"/><path d="M0 0l7 5 7-5" stroke="#060606" fill="none"/></svg><p>support@parcelohome.com</p></div>
    </div>
    <div class="fcol" style="width:260px;padding-left:20px">
      <h4>Newslatter Signup</h4>
      <p>Signup with us and get update in your inbox.</p>
      <div class="input">Your Name</div>
      <div class="input">Email address</div>
      <span class="sub-btn">Subscribe</span>
    </div>
    <div class="fcol" style="width:170px;padding-left:20px">
      <h4>Social Connect</h4>
      <ul class="social"><li><i></i>Friendly</li><li><i></i>Chirper</li><li><i></i>Worknet</li></ul>
    </div>
  </div>
</footer>
<div class="bottombar"><span class="pay">Paywise</span><span>Copyright © 2014 - Parcelo Home</span></div>

</body>
</html>
```